Corporate Business Card

Very professional, Modern, Not to busy, include phone address email, website
(253) 555-0174, 61807 19th Street N, Kent, WA 98517, marcus@kestrelbayholding.com, brelvanindustries.com

Target Market(s)

Manufacturing

Industry/Entity Type

Aero, machining, manufacturing, Off road racing

Contact Information for Business Card

Phone, address email, website

```html
<!DOCTYPE html>
<html lang="en">
<head>
<meta charset="utf-8">
<title>Brelvan Industries – Business Card</title>
<link rel="stylesheet" href="https://fonts.googleapis.com/css2?family=Inter:wght@400;500;600;800&display=swap">
<style>
  :root {
    --page-bg: #fdf4f2;
    --card-bg: #ffffff;
    --navy: #1f3a78;
    --red: #d9312b;
    --stripe-blue: #e9ecf4;
    --stripe-pink: #fbeee9;
    --glow: rgba(240, 160, 140, 0.28);
  }
  * { box-sizing: border-box; margin: 0; padding: 0; }
  html, body {
    width: 1200px; height: 1200px; overflow: hidden;
    background: var(--page-bg);
    font-family: "Inter", sans-serif;
  }
  .stage { position: relative; width: 1200px; height: 1200px; }
  .card {
    position: absolute; left: 218px; width: 764px; height: 435px;
    background: var(--card-bg); border-radius: 22px; overflow: hidden;
    box-shadow: 0 0 22px 6px var(--glow);
  }
  .card--front { top: 129px; }
  .card--back { top: 657px; }
  .card__stripes { position: absolute; left: 0; top: 0; }
  .brand {
    position: absolute; display: flex; align-items: center; gap: 10px;
    color: var(--navy); font-weight: 800; white-space: nowrap; letter-spacing: -0.01em;
  }
  .brand__mark { background: var(--red); display: block; }
  .card--front .brand { left: 94px; top: 188px; font-size: 28px; }
  .card--front .brand__mark { width: 16px; height: 16px; }
  .card--back .brand {
    left: 50%; top: 50%; transform: translate(-50%, -50%); font-size: 44px; gap: 14px;
  }
  .card--back .brand__mark { width: 24px; height: 24px; }
  .person { position: absolute; left: 404px; top: 72px; }
  .person__name { color: var(--red); font-size: 26px; font-weight: 600; line-height: 1.2; }
  .person__title { color: var(--navy); font-size: 20px; font-weight: 500; margin-top: 4px; }
  .contact { position: absolute; left: 390px; top: 190px; list-style: none; }
  .contact__item {
    display: flex; align-items: flex-start; gap: 12px;
    color: var(--navy); font-size: 21px; line-height: 1.3; margin-bottom: 12px;
  }
  .contact__icon { flex: 0 0 16px; width: 16px; height: 16px; margin-top: 5px; fill: var(--red); }
</style>
</head>
<body>
<main class="stage">
  <section class="card card--front">
    <svg class="card__stripes" width="764" height="435" viewBox="0 0 764 435" aria-hidden="true">
      <polygon points="62,0 132,0 225,100 155,100" fill="var(--stripe-blue)"/>
      <polygon points="0,0 40,0 153,133 113,133" fill="var(--stripe-pink)"/>
      <polygon points="0,70 0,125 88,178 40,178" fill="var(--stripe-pink)"/>
    </svg>
    <div class="brand"><span class="brand__mark"></span>Brelvan Industries</div>
    <div class="person">
      <p class="person__name">Daniel Reyes</p>
      <p class="person__title">Founder &amp; CEO</p>
    </div>
    <ul class="contact">
      <li class="contact__item">
        <svg class="contact__icon" viewBox="0 0 16 16"><path d="M8 0a6 6 0 0 0-6 6c0 4.5 6 10 6 10s6-5.5 6-10a6 6 0 0 0-6-6zm0 8.5A2.5 2.5 0 1 1 8 3.5a2.5 2.5 0 0 1 0 5z"/></svg>
        <span>61807 19th Street N, Kent,<br>WA 98517,</span>
      </li>
      <li class="contact__item">
        <svg class="contact__icon" viewBox="0 0 16 16"><path d="M3.6 1l2.3 3-1.3 1.6c.9 2 2.6 3.8 4.8 4.8L11 9.1l3 2.3-1.4 2.8C7 14 2 9 1.8 3.4z"/></svg>
        <span>(253) 555-0174</span>
      </li>
      <li class="contact__item">
        <svg class="contact__icon" viewBox="0 0 16 16"><path d="M1 3h14v1.5L8 9 1 4.5z M1 6.3l7 4.5 7-4.5V13H1z"/></svg>
        <span>marcus@kestrelbayholding.com</span>
      </li>
      <li class="contact__item">
        <svg class="contact__icon" viewBox="0 0 16 16"><path d="M8 1a7 7 0 1 0 0 14A7 7 0 0 0 8 1zm0 1.6c.8.9 1.4 2.2 1.6 3.6H6.4C6.6 4.8 7.2 3.5 8 2.6zM2.7 7.4h2.4c0 .4 0 .8.1 1.2H2.7a5 5 0 0 1 0-1.2zm.5 2.4h2.2c.2 1.2.6 2.3 1.1 3.2a5.4 5.4 0 0 1-3.3-3.2zm3.2 0h3.2C9.4 11.2 8.8 12.5 8 13.4c-.8-.9-1.4-2.2-1.6-3.6zm3.7 3.2c.5-.9.9-2 1.1-3.2h2.2a5.4 5.4 0 0 1-3.3 3.2zm1.3-4.4c.1-.4.1-.8.1-1.2h2.4a5 5 0 0 1 0 1.2zM6.3 7.4h3.4v1.2H6.3zm4.6-1.2c-.2-1.2-.6-2.3-1.1-3.2a5.4 5.4 0 0 1 3.3 3.2zm-5.8 0H2.9A5.4 5.4 0 0 1 6.2 3c-.5.9-.9 2-1.1 3.2z"/></svg>
        <span>brelvanindustries.com</span>
      </li>
    </ul>
  </section>
  <section class="card card--back">
    <div class="brand"><span class="brand__mark"></span>Brelvan Industries</div>
  </section>
</main>
</body>
</html>
```